Web design project for exciting Australian start-up

Background
We are looking for a creative and talented web design artist to work alongside our market leading web developer.
• You will be required to create a modern and clean design theme for our website, incorporating selected rustic colour scheme elements for our exciting Australian start-up to operate within the coffee industry.
reoccurring work to be expected to flow to the successful designer.
Requirements
• c. 5 - 10 page website
• Landing page
• Log in/ out
• 404 template
• Typography is emphasised
• Please use either a) typevane.com, b) free web fonts, c) marlo fonts
• All design elements in vector format
• Preferably with icons for each header title(i.e. about us, how it works etc) but designer have free reign over how the site looks, so might not be applicable
• All pages to be responsive
• Down to iPad resolution

High level visual design brief attached - additional pages to be worked from base design.

Design inspiration
• We would like to use design elements from the following sources:
http://www.brivantel.com/sorvik/ (Functionality)
Colour scheme refer to logo and complementary style guide
Updates

```html
<!DOCTYPE html>
<html lang="en">
<head>
<meta charset="utf-8">
<title>Roastwell – Dashboard</title>
<link href="https://fonts.googleapis.com/css2?family=Roboto:wght@300;400;500;700&display=swap" rel="stylesheet">
<style>
:root{
  --dark:#47494b;
  --orange:#f39a33;
  --orange-soft:#f6a84f;
  --panel:#f2f2f2;
  --line:#e3e3e3;
  --text:#222;
  --muted:#8e8e8e;
  --faint:#a9a9a9;
  --footer:#e9e9e9;
  --page:#fafafa;
}
*{box-sizing:border-box;margin:0;padding:0}
html,body{width:1200px;height:990px;overflow:hidden}
body{font-family:"Roboto",Arial,sans-serif;background:var(--page);color:var(--text);position:relative}
.site-header{height:85px;border-bottom:1px solid #e5e5e5;background:#f7f7f7;position:relative}
.brand{position:absolute;left:52px;top:24px;display:flex;align-items:center;gap:8px;font-weight:700;font-size:20px;color:var(--text);letter-spacing:1px}
.brand-dot{width:34px;height:34px;border-radius:50%;background:var(--orange)}
.main-nav{position:absolute;right:52px;top:28px;display:flex;align-items:center;gap:24px;font-size:12.5px;color:#666}
.logout{background:var(--dark);color:#fff;padding:7px 10px;border:1px solid #333;display:flex;align-items:center;gap:6px;font-size:12.5px}
.col{position:absolute;top:102px}
.col-left{left:52px;width:275px}
.col-mid{left:338px;width:523px}
.col-right{left:874px;width:274px}
.bar{height:37px;background:var(--dark);color:#fff;display:flex;align-items:center;padding:0 9px;gap:8px;font-size:16px;letter-spacing:-.3px}
.bar.accent{color:var(--orange)}
.arrows{margin-left:auto;display:flex;gap:5px}
.arrows span{width:24px;height:24px;background:#fff;color:var(--orange);display:flex;align-items:center;justify-content:center;font-size:14px;font-weight:700}
.photo{height:200px;background:radial-gradient(ellipse 95px 58px at 50% 45%,#6b4a36 0,#a08170 35%,#f4f2f0 62%,#e6e6e6 80%,var(--panel) 100%)}
.cafe-row{height:49px;background:var(--panel);display:flex;align-items:center;justify-content:space-between;padding:0 8px;border-top:1px solid var(--line)}
.cafe-name{color:var(--orange);font-size:14px}
.cafe-date{display:flex;align-items:center;gap:5px;font-size:13px;color:#666}
.member{background:#fff;padding:18px 8px;font-size:16.5px;line-height:24px;height:81px}
.gap{height:22px}
.acct-item{background:var(--panel);padding:14px 8px;border-bottom:1px solid var(--line);height:76px}
.acct-item h4{font-weight:400;font-size:15.5px;margin-bottom:8px}
.acct-item p{font-size:13.5px;color:var(--muted)}
.drop{display:flex;align-items:center;gap:8px;font-size:14px;color:#555}
.tri{width:0;height:0;border-left:5px solid transparent;border-right:5px solid transparent;border-top:7px solid #999}
.tri.white{border-top-color:#fff}
.time{height:47px;background:#fff;padding:0 12px;display:flex;align-items:center}
.tender{height:76px;background:var(--panel);padding:15px 10px}
.tender b{font-weight:400;font-size:14px;display:block;margin-bottom:10px}
.tender span{font-size:13px;color:#777}
.filters{height:47px;background:var(--orange-soft);display:grid;grid-template-columns:195px 160px 1fr;color:#fff;font-size:14.5px}
.filters div{display:flex;align-items:center;gap:8px;padding:0 12px;border-right:1px solid #e8912f}
.filters div:last-child{border:none;padding:0 8px 0 16px}
table{width:100%;border-collapse:collapse;font-size:13px;color:var(--faint);font-weight:300}
td{height:40.7px;padding:0 10px;border:1px solid var(--line)}
tr:nth-child(odd){background:var(--panel)}
tr:nth-child(even){background:#fff}
.inbox-menu{height:71px;background:var(--panel);padding:16px 10px;display:flex;flex-direction:column;gap:8px;font-size:13.5px;color:var(--muted)}
.inbox-menu .drop{color:var(--muted)}
.week{height:38px;background:#fff;display:flex;align-items:center;justify-content:space-between;padding:0 10px;font-size:15.5px;border-top:1px solid var(--line);border-bottom:1px solid var(--line)}
.lt,.rt{width:0;height:0;border-top:5px solid transparent;border-bottom:5px solid transparent}
.lt{border-right:8px solid #555}.rt{border-left:8px solid #555}
.deliveries{height:164px;background:var(--panel);position:relative}
.delivery{padding:9px 8px;border-bottom:1px solid var(--line);height:71px;margin-right:10px}
.delivery b{color:var(--orange);font-weight:400;font-size:14px;display:block;margin-bottom:5px}
.delivery span{font-size:12.5px;color:var(--muted);display:block;line-height:16px}
.scroll{position:absolute;right:2px;top:8px;bottom:2px;width:7px;border:1px solid #ccc;background:#fff}
.scroll i{position:absolute;left:0;right:0;top:80px;height:14px;background:#ddd}
.calendar{margin-top:24px;background:#e4e4e4;border:1px solid #ccc}
.cal-head{height:43px;background:var(--dark);display:flex;align-items:center;justify-content:space-between;padding:0 22px;color:#fff;font-size:16.5px}
.cal-head .lt{border-right-color:#fff}.cal-head .rt{border-left-color:#fff}
.cal-grid{display:grid;grid-template-columns:repeat(7,1fr)}
.cal-grid span{height:39.3px;display:flex;align-items:center;justify-content:center;font-size:15px;font-weight:500;color:#333;border-right:1px solid #fff;border-bottom:1px solid #fff;background:#e2e2e2}
.cal-grid .wd{font-weight:300;color:#999;height:35px;background:#dcdcdc}
.cal-grid .off{color:#999}
.cal-grid .today{background:var(--orange);color:#fff}
.download{height:46px;background:var(--panel);display:flex;align-items:center;gap:6px;padding:0 8px;color:var(--orange);font-size:16px;border:1px solid var(--line);border-top:none}
.site-footer{position:absolute;left:0;top:792px;width:1200px;height:198px;background:var(--footer);font-size:12.5px;color:#555}
.site-footer h5{font-size:14px;font-weight:400;color:#111;margin-bottom:16px}
.fcol{position:absolute;top:34px}
.fcol p{line-height:16.7px;font-weight:300;width:300px}
.fcol a{display:block;color:#333;font-size:13.5px;margin-bottom:6px;text-decoration:none;font-weight:300}
.social a{display:flex;align-items:center;gap:8px;font-size:14.5px;margin-bottom:10px}
.social i{width:18px;height:18px;border-radius:50%;background:#999}
.foot-brand{position:absolute;left:962px;top:58px;display:flex;align-items:center;gap:8px;font-weight:700;font-size:19px;color:#555;letter-spacing:1px}
.foot-brand i{width:30px;height:30px;border-radius:50%;background:#aaa}
.copy{position:absolute;left:961px;top:115px;font-size:13px;color:#444}
</style>
</head>
<body>
<header class="site-header">
  <div class="brand"><span class="brand-dot"></span>ROASTWELL</div>
  <nav class="main-nav">
    <span>HOME</span><span>ABOUT US</span><span>MARKETPLACE</span><span>LOGGED IN</span>
    <span class="logout"><svg width="16" height="14" viewBox="0 0 16 14"><path d="M9 2.5A5 5 0 1 0 9 11.5" fill="none" stroke="#fff" stroke-width="1.8"/><path d="M6 7h9M12 4l3 3-3 3" fill="none" stroke="#fff" stroke-width="1.8"/></svg>LOGOUT</span>
  </nav>
</header>

<section class="col col-left">
  <div class="bar accent"><svg width="18" height="16" viewBox="0 0 18 16"><rect x="1" y="1" width="12" height="10" fill="none" stroke="#fff" stroke-width="1.5"/><rect x="4" y="4" width="12" height="10" fill="none" stroke="#fff" stroke-width="1.5"/></svg>Photos
    <div class="arrows"><span>‹</span><span>›</span></div></div>
  <div class="photo" role="img" aria-label="Photo of a chocolate dessert on a white plate"></div>
  <div class="cafe-row"><span class="cafe-name">CAFE AMBROSE</span>
    <span class="cafe-date"><svg width="20" height="19" viewBox="0 0 20 19"><rect x="1" y="3" width="18" height="15" fill="none" stroke="#777" stroke-width="1.4"/><path d="M1 7h18M5 1v4M15 1v4" stroke="#777" stroke-width="1.4"/><text x="10" y="16" font-size="8" text-anchor="middle" fill="#777" font-family="Roboto,sans-serif">10</text></svg>Feb,2014</span></div>
  <div class="member">Melbourne, Australia<br>Member Since [Feb,2014]</div>
  <div class="gap"></div>
  <div class="bar accent"><svg width="20" height="18" viewBox="0 0 20 18"><circle cx="7" cy="5" r="4" fill="#fff"/><path d="M0 17c0-5 3-7 7-7s7 2 7 7z" fill="#fff"/><circle cx="15" cy="13" r="3" fill="none" stroke="#fff" stroke-width="1.6"/></svg>My Account</div>
  <div class="acct-item"><h4>Email Address</h4><p>...Verified</p></div>
  <div class="acct-item"><h4>Cafe Type</h4><p>(i.e. Cafe,speciality coffee shop,restaurant)</p></div>
  <div class="acct-item" style="height:67px"><h4>Cafe Type</h4><p>Verified</p></div>
</section>

<section class="col col-mid">
  <div class="bar"><svg width="18" height="18" viewBox="0 0 18 18"><path d="M3 8a6 6 0 0 1 11-3M15 10a6 6 0 0 1-11 3" fill="none" stroke="#fff" stroke-width="2"/><path d="M14 1v5h-5M4 17v-5h5" fill="none" stroke="#fff" stroke-width="2"/></svg>Live Tenders</div>
  <div class="time"><span class="drop"><i class="tri"></i>Time remaining</span></div>
  <div class="tender"><b>8 am - 11 am</b><span>Delivery of order 3220x&nbsp; Order: 20kg Highland Beans</span></div>
  <div class="bar" style="margin-top:1px"><svg width="20" height="18" viewBox="0 0 20 18"><path d="M1 1h3l3 11h10l2-8H5" fill="none" stroke="#fff" stroke-width="1.8"/><circle cx="8" cy="16" r="1.5" fill="#fff"/><circle cx="16" cy="16" r="1.5" fill="#fff"/></svg>Purchases</div>
  <div class="filters">
    <div><i class="tri white"></i>All</div>
    <div><i class="tri white"></i>Period (x months)</div>
    <div><i class="tri white"></i>A waiting feedback (x)</div>
  </div>
  <table>
    <colgroup><col style="width:195px"><col style="width:156px"><col></colgroup>
    <tr><td>Lorem ipsum dolor sit amet</td><td>dd/mm/yyyy</td><td>10,Feb ,2014</td></tr>
    <tr><td>Lorem ipsum dolor sit amet</td><td>dd/mm/yyyy</td><td>10,Feb ,2014</td></tr>
    <tr><td>Lorem ipsum dolor sit amet</td><td>dd/mm/yyyy</td><td>10,Feb ,2014</td></tr>
    <tr><td>Lorem ipsum dolor sit amet</td><td>dd/mm/yyyy</td><td>10,Feb ,2014</td></tr>
    <tr><td>Lorem ipsum dolor sit amet</td><td>dd/mm/yyyy</td><td>10,Feb ,2014</td></tr>
    <tr><td>Lorem ipsum dolor sit amet</td><td>dd/mm/yyyy</td><td>10,Feb ,2014</td></tr>
    <tr><td>Lorem ipsum dolor sit amet</td><td>dd/mm/yyyy</td><td>10,Feb ,2014</td></tr>
    <tr><td>Lorem ipsum dolor sit amet</td><td>dd/mm/yyyy</td><td>10,Feb ,2014</td></tr>
    <tr><td>Lorem ipsum dolor sit amet</td><td>dd/mm/yyyy</td><td>10,Feb ,2014</td></tr>
    <tr><td>Lorem ipsum dolor sit amet</td><td>dd/mm/yyyy</td><td>10,Feb ,2014</td></tr>
  </table>
</section>

<section class="col col-right">
  <div class="bar"><svg width="20" height="18" viewBox="0 0 20 18"><path d="M1 7l9-6 9 6v10H1z" fill="none" stroke="#fff" stroke-width="1.6"/><path d="M1 7l9 6 9-6" fill="none" stroke="#fff" stroke-width="1.6"/><rect x="5" y="4" width="10" height="5" fill="#fff"/></svg>Inbox</div>
  <div class="inbox-menu"><span class="drop"><i class="tri"></i>Messages</span><span class="drop"><i class="tri"></i>Saved Searches</span></div>
  <div class="week"><i class="lt"></i>Incoming Deliveries this week<i class="rt"></i></div>
  <div class="deliveries">
    <div class="delivery"><b>8 am - 11 am</b><span>Delivery of order 3220x</span><span>Order: 20kg Highland Beans</span></div>
    <div class="delivery"><b>8 am - 11 am</b><span>Delivery of order 3220x</span><span>Order: 20kg Highland Beans</span></div>
    <div class="scroll"><i></i></div>
  </div>
  <div class="calendar">
    <div class="cal-head"><i class="lt"></i>Novembre 2014<i class="rt"></i></div>
    <div class="cal-grid">
      <span class="wd">M</span><span class="wd">T</span><span class="wd">W</span><span class="wd">T</span><span class="wd">F</span><span class="wd">S</span><span class="wd">S</span>
      <span class="off">28</span><span>1</span><span>2</span><span>3</span><span class="today">4</span><span>5</span><span>6</span>
      <span>7</span><span>8</span><span>9</span><span>10</span><span>11</span><span>12</span><span>13</span>
      <span>14</span><span>15</span><span>16</span><span>17</span><span>18</span><span>19</span><span>20</span>
      <span>21</span><span>22</span><span>23</span><span>24</span><span>25</span><span>26</span><span>27</span>
      <span>28</span><span>29</span><span>30</span><span>31</span><span class="off">1</span><span class="off">2</span><span class="off">3</span>
    </div>
  </div>
  <div class="download"><svg width="18" height="18" viewBox="0 0 18 18"><circle cx="9" cy="9" r="8" fill="none" stroke="#333" stroke-width="1.5"/><path d="M9 4v8M5.5 9L9 12.5 12.5 9" fill="none" stroke="#333" stroke-width="1.6"/></svg>Download</div>
</section>

<footer class="site-footer">
  <div class="fcol" style="left:52px"><h5>ABOUT US</h5>
    <p>Lorem ipsum dolor sit amet, consectetur adipisicing elit, sed do eiusmod tempor incididunt ut labore et dolore magna aliqua. Ut enim ad minim veniam, quis nostrud exercitation ullamco laboris nisi ut aliquip ex ea commodo consequat. Duis aute irure dolor in reprehenderit in voluptate velit esse cillum dolore eu fugiat nulla pariatur.</p></div>
  <div class="fcol" style="left:429px"><h5>HELPFUL INFO</h5><a>About us</a><a>Media Enquiries</a><a>Terms &amp; Conditions</a><a>Privacy Policy</a></div>
  <div class="fcol" style="left:618px"><h5>WHO WE ARE</h5><a>How It Works</a><a>Faq</a><a>Contact Us</a></div>
  <div class="fcol social" style="left:788px"><h5>FOLLOW US</h5>
    <a><i></i>Friendloop</a><a><i></i>Worknet</a><a><i></i>Friendloop</a><a><i></i>Worknet</a></div>
  <div class="foot-brand"><i></i>ROASTWELL</div>
  <div class="copy">Copyright © 2014 Roastwell.</div>
</footer>
</body>
</html>
```